indoor tennis and sports center( club)

we need a logo for a new business venture, it will be for business cards and for presentations.
presentations for potential investors and authorities.
the design needs to communicate the sport and a community of tennis players
the center includes a tennis academy, and sports club with training sessions for all ages

Reason: so that I can get some more feedback on my side as to te design we want

Target Market(s)

potential investors or partners

Industry/Entity Type

Business

Contact Information for Business Card

i need the name of the club
names of the partners
slogan" changing lives through tennis" on the front
the clubs three main goals are ports education , academy and a community club

Colors
3176b5
33b8a4
fbee3d
0dac94
acd036

Requirements
Must have
• a strong logo
• names of the partners
• web site and email address
• tel number
Nice to have
• a connection between the different aspects of the club

```html
<!DOCTYPE html>
<html lang="en">
<head>
<meta charset="utf-8">
<title>Baseline Hall – Business Card</title>
<link href="https://fonts.googleapis.com/css2?family=Open+Sans:wght@300;400&family=Marcellus+SC&family=Oswald:wght@500&display=swap" rel="stylesheet">
<style>
  :root {
    --teal: #0f8ea3;
    --teal-dark: #0a6f80;
    --teal-light: #18a6bb;
    --paper: #ffffff;
    --ink: #3a3a3a;
    --muted: #6d6d6d;
    --backdrop: #e9e6e1;
  }
  * { box-sizing: border-box; margin: 0; padding: 0; }
  html, body { width: 771px; height: 1200px; overflow: hidden; }
  body {
    background: var(--backdrop);
    font-family: "Open Sans", Arial, sans-serif;
    display: flex;
    flex-direction: column;
    align-items: center;
    justify-content: space-around;
    padding: 60px 0;
  }
  .card {
    position: relative;
    width: 630px;
    height: 360px;
    border-radius: 3px;
    box-shadow: 0 10px 28px rgba(0,0,0,.18);
    overflow: hidden;
  }

  /* Front */
  .card--front { background: var(--paper); color: var(--ink); }
  .brand {
    position: absolute;
    top: 44px;
    right: 46px;
    display: flex;
    align-items: center;
    gap: 10px;
    font-family: "Open Sans", Arial, sans-serif;
    font-weight: 400;
    font-size: 22px;
    color: var(--teal);
  }
  .brand__dot {
    width: 26px; height: 26px;
    border-radius: 50%;
    background: var(--teal);
  }
  .holder {
    position: absolute;
    left: 46px;
    top: 150px;
    padding-left: 12px;
    border-left: 4px solid var(--teal);
  }
  .holder__name { font-size: 30px; font-weight: 400; line-height: 1.1; color: var(--ink); }
  .holder__title { font-size: 17px; font-weight: 300; color: var(--teal); margin-top: 2px; }
  .contacts {
    position: absolute;
    left: 50px;
    bottom: 40px;
    list-style: none;
    font-size: 13px;
    font-weight: 300;
    color: var(--muted);
  }
  .contacts li { display: flex; align-items: center; gap: 10px; margin-top: 7px; }
  .contacts svg { width: 14px; height: 14px; fill: var(--teal); }
  .slogan {
    position: absolute;
    right: 46px;
    bottom: 70px;
    font-family: "Marcellus SC", Georgia, serif;
    font-size: 21px;
    color: var(--ink);
  }
  .slogan__accent { color: var(--teal); }

  /* Back */
  .card--back {
    background: linear-gradient(160deg, var(--teal-light) 0%, var(--teal) 50%, var(--teal-dark) 100%);
    color: var(--paper);
  }
  .back-brand {
    position: absolute;
    left: 60px;
    top: 130px;
    display: flex;
    align-items: center;
    gap: 14px;
    font-family: "Open Sans", Arial, sans-serif;
    font-weight: 400;
    font-size: 34px;
    color: var(--paper);
  }
  .back-brand__dot { width: 40px; height: 40px; border-radius: 50%; background: var(--paper); }
  .back-brand__sub {
    position: absolute;
    left: 114px;
    top: 182px;
    font-size: 12px;
    letter-spacing: .5px;
    text-transform: uppercase;
    color: rgba(255,255,255,.9);
  }
  .pillars {
    position: absolute;
    right: 46px;
    top: 112px;
    font-family: "Oswald", "Arial Narrow", sans-serif;
    font-weight: 500;
    font-size: 15px;
    letter-spacing: .5px;
    text-transform: uppercase;
  }
  .pillars span { margin: 0 6px; opacity: .85; }
  .tagline {
    position: absolute;
    right: 46px;
    top: 140px;
    font-family: "Marcellus SC", Georgia, serif;
    font-size: 22px;
  }
</style>
</head>
<body>

  <section class="card card--front" aria-label="Business card front">
    <div class="brand"><span class="brand__dot"></span>Baseline Hall</div>

    <div class="holder">
      <p class="holder__name">Your Name</p>
      <p class="holder__title">Job Title</p>
    </div>

    <ul class="contacts">
      <li>
        <svg viewBox="0 0 16 16" aria-hidden="true"><path d="M2 4c0-1 1-2 2-2h8c1 0 2 1 2 2v1h-3V4H5v1H2zM3 6h10l1 7H2zM8 8a2 2 0 1 0 0 4a2 2 0 0 0 0-4z"/></svg>
        000 000 0000
      </li>
      <li>
        <svg viewBox="0 0 16 16" aria-hidden="true"><path d="M1 3h14v10H1zM2 4l6 5l6-5v1l-6 5l-6-5z" fill-rule="evenodd"/></svg>
        youremail@xyz.com
      </li>
      <li>
        <svg viewBox="0 0 16 16" aria-hidden="true"><circle cx="8" cy="8" r="7" fill="none" stroke="#0f8ea3" stroke-width="1.4"/><ellipse cx="8" cy="8" rx="3" ry="7" fill="none" stroke="#0f8ea3" stroke-width="1.2"/><path d="M1 8h14" stroke="#0f8ea3" stroke-width="1.2"/></svg>
        www.yourwebsite.com
      </li>
    </ul>

    <p class="slogan">Changing <span class="slogan__accent">lives</span> through Tennis</p>
  </section>

  <section class="card card--back" aria-label="Business card back">
    <div class="back-brand"><span class="back-brand__dot"></span>Baseline Hall</div>
    <p class="back-brand__sub">Coastal Indoor Racquet and Sports Club</p>

    <p class="pillars">Indoor Club<span>|</span>Academy<span>|</span>Education</p>
    <p class="tagline">Building a community</p>
  </section>

</body>
</html>
```